Solar and energy efficient equipment finance introduction and product flyer

Were a specialty provider of finance solutions for solar and energy efficient equipment. Our customers (the people and businesses that get the equipment installed on their properties) use our solutions to get equipment for $0 upfront. Even better then paying nothing upfront, they can often pay for the systems via the savings generated - meaning they are cash flow positive immediately.

The attached presentation is to introduce OUR FIRM to solar and energy efficient equipment retailers and installers (our distributors). These distributors then offer our finance to their customers to help secure sales.

As such the audience for this document is solar installers and distributors. We are looking for a fresh look that says:

- we get understand the technology,
- we're agile and highly responsive,
- we create unique value adding solutions, and
- we're totally reliable.

We also want to update the attached flyer(s) to match stylistically. In this instance the template will introduce OUR PRODUCTS to distributor AND customers.

Target Market(s)

Solar and energy efficient equipment finance retailers and installers

Industry/Entity Type

Finance

Font styles to use
Serif

Colors
f37022
0255a3

Requirements
Must have
• Template functionality

```html
<!DOCTYPE html>
<html lang="en">
<head>
<meta charset="utf-8">
<title>Brightpath Rental – Our Rental Solution Explained</title>
<link rel="stylesheet" href="https://fonts.googleapis.com/css2?family=Open+Sans:wght@600;700;800&family=Ubuntu:wght@400;500&display=swap">
<style>
  :root{
    --green:#1fa24a;
    --blue:#2a5aa7;
    --gold:#e6a72c;
    --ink:#2b2f48;
    --paper:#ffffff;
    --stage:#e4e4e4;
  }
  *{box-sizing:border-box;margin:0;padding:0}
  html,body{width:1200px;height:1000px;overflow:hidden}
  body{background:var(--stage);font-family:"Ubuntu",sans-serif;color:var(--ink)}
  .flyer{
    position:absolute;left:260px;top:20px;width:680px;height:960px;
    background:var(--paper);border-top:3px solid var(--gold);
    box-shadow:0 4px 18px rgba(0,0,0,.15);
  }
  .flyer > *{position:absolute}
  .top-notch{left:332px;top:0;width:0;height:0;border-left:7px solid transparent;border-right:7px solid transparent;border-top:7px solid var(--gold)}

  .brand{left:0;right:0;top:40px;display:flex;justify-content:center;align-items:center;gap:12px}
  .brand-dot{width:44px;height:44px;border-radius:50%;background:var(--blue)}
  .brand-name{font-family:"Ubuntu",sans-serif;font-weight:500;font-size:30px;color:var(--blue)}

  .band{height:34px;display:flex;align-items:center;color:#fff;font-family:"Open Sans",sans-serif;font-weight:700;text-transform:uppercase}
  .band::before{content:"";position:absolute;inset:0;z-index:0;clip-path:polygon(0 0,calc(100% - 26px) 0,calc(100% - 6px) 100%,0 100%)}
  .band::after{content:"";position:absolute;top:0;right:-8px;width:9px;height:100%;transform:skewX(34deg);transform-origin:top}
  .band span{position:relative;z-index:1}
  .band--green::before{background:var(--green)}
  .band--green::after{background:var(--blue)}
  .band--blue::before{background:var(--blue)}
  .band--blue::after{background:var(--gold)}
  .band--gold::before{background:var(--gold)}
  .band--gold::after{background:var(--blue)}

  .band--title{left:0;top:122px;width:443px;font-size:19px;padding-left:32px;letter-spacing:.3px}
  .headline{left:0;right:0;top:178px;text-align:center;font-family:"Open Sans",sans-serif;font-weight:800;font-size:62px;color:var(--green);letter-spacing:-.5px}
  .claims{left:158px;top:256px;width:364px;height:34px;padding:2px 0 0 12px;border-left:2px solid var(--green);border-right:2px solid var(--green);font-family:"Open Sans",sans-serif;font-weight:600;font-size:13px;line-height:15px;color:var(--green);text-transform:uppercase}
  .claims::before,.claims::after{content:"";position:absolute;width:8px;top:0;bottom:0;border-top:2px solid var(--green);border-bottom:2px solid var(--green)}
  .claims::before{left:-2px}
  .claims::after{right:-2px}

  .band--section{height:24px;font-size:16px;font-weight:600;padding-left:34px}
  .band--why{left:0;top:323px;width:198px}
  .band--how{left:0;top:584px;width:243px}

  .copy{font-size:12.5px;line-height:15.5px}
  .copy p + p{margin-top:15px}
  .copy--why{left:38px;top:356px;width:260px}
  .copy--how{left:46px;top:620px;width:250px}

  .benefits{left:370px;top:323px;width:305px;height:198px;background:var(--blue);color:#fff;padding:10px 0 0 34px}
  .benefits::before{content:"";position:absolute;left:0;top:0;width:7px;height:100%;background:var(--gold);transform:skewX(-3deg);transform-origin:bottom}
  .benefits h2{font-family:"Open Sans",sans-serif;font-weight:600;font-size:16px;text-transform:uppercase;margin-bottom:10px}
  .benefits ul{font-size:10.3px;line-height:16.7px;padding-left:12px}

  .pay-title{left:350px;top:594px;width:325px;height:18px;display:flex;align-items:center;gap:8px;font-family:"Open Sans",sans-serif;font-weight:600;font-size:16px;color:var(--green);text-transform:uppercase}
  .pay-title::before{content:"";width:20px;height:10px;background:var(--green)}
  .pay-title::after{content:"";flex:1;height:10px;background:var(--green)}

  .box{display:flex;align-items:center;justify-content:center;text-align:center;border:2px solid;border-radius:6px;font-family:"Open Sans",sans-serif;font-weight:700;font-size:11px;line-height:12.5px;text-transform:uppercase}
  .box--without{left:354px;top:622px;width:104px;height:244px;border-color:var(--green);color:var(--green)}
  .box--rental{left:470px;top:709px;width:155px;height:74px;border-color:var(--blue);color:var(--blue);font-weight:600}
  .box--with{left:470px;top:793px;width:155px;height:73px;border-color:var(--gold);color:var(--gold)}
  .savings-arrow{left:463px;top:620px;width:164px;height:82px}
</style>
</head>
<body>
  <main class="flyer">
    <div class="top-notch"></div>

    <header class="brand">
      <div class="brand-dot"></div>
      <div class="brand-name">Brightpath Rental</div>
    </header>

    <div class="band band--green band--title"><span>Our Rental Solution Explained</span></div>
    <h1 class="headline">$0 UPFRONT</h1>
    <div class="claims">- Immediate savings on your electricity bills<br>- Repayments may be fully deductible</div>

    <div class="band band--blue band--section band--why"><span>Why Finance?</span></div>
    <div class="copy copy--why">
      <p>A major reason why many businesses don’t install energy saving equipment on their premises is due to the large upfront cost of the solutions themselves.</p>
      <p>So we’ve teamed up with industry specialist Brightpath Rental to provide our customers with a financing plan that lets you install a range of energy saving solutions without a large upfront payment while letting you enjoy an immediately lower electricity bill.</p>
    </div>

    <section class="benefits">
      <h2>Benefits</h2>
      <ul>
        <li>No deposit (Includes installation &amp; design)</li>
        <li>Immediate savings on your bills</li>
        <li>Flexible terms up to 7 years</li>
        <li>Repayments may be fully tax deductible</li>
        <li>Option to buy at the end of rental</li>
        <li>Low Doc options available</li>
        <li>48 hour approval</li>
        <li>Installation and manufacturing warranties<br>(Up to 25 years for Solar PV systems)</li>
      </ul>
    </section>

    <div class="band band--gold band--section band--how"><span>How does it work?</span></div>
    <div class="copy copy--how">
      <p>Once installed, your lower energy bill plus the rental payments is in most cases less than your old electricity bill.</p>
      <p>You pay the system off over time – from 2 to 7 years (just like you rent a mobile phone).</p>
      <p>This way you can often start saving from the day your system is installed.</p>
      <p>So you can now get the benefits of reduced electricity bills for $0 upfront.</p>
      <p>There are no costs to up front,<br>so get started today!</p>
    </div>

    <div class="pay-title">Pay via savings generated</div>
    <div class="box box--without">Energy bill<br>without<br>solar or<br>energy<br>efficient<br>equipment</div>
    <svg class="savings-arrow" viewBox="0 0 164 82" aria-hidden="false" role="img" aria-label="Arrow: you could save money from day 1">
      <polygon points="34,2 130,2 130,38 162,38 82,80 2,38 34,38" fill="none" stroke="#2a5aa7" stroke-width="2" stroke-linejoin="round"/>
      <text x="82" y="26" text-anchor="middle" font-family="Open Sans, sans-serif" font-weight="700" font-size="9.5" fill="#2a5aa7">YOU COULD</text>
      <text x="82" y="38" text-anchor="middle" font-family="Open Sans, sans-serif" font-weight="700" font-size="9.5" fill="#2a5aa7">SAVE MONEY</text>
      <text x="82" y="50" text-anchor="middle" font-family="Open Sans, sans-serif" font-weight="700" font-size="9.5" fill="#2a5aa7">FROM DAY 1</text>
    </svg>
    <div class="box box--rental">Rental payment</div>
    <div class="box box--with">Energy bill<br>with solar or<br>energy efficient<br>equipment</div>
  </main>
</body>
</html>
```